Webpage for a treatment housing for young addicts.

I need a new design and files for my wordpress page. I need it to be more neat and clean. I need it to look professional with a starting page that will work as a navigation. I need like logo and phone number and such up top, a picture under it with one sentence as a slogan and under it 6 boxes to click to come to our different pages. Under it I want news etc.

Target Market(s)

Social services, employees and governements

Coding

Coded - Design and coding required

Font styles to use
Sans Serif

Colors
abd037
3176b5
9d9d9d
aaaaaa
f04a50

Requirements
Must have
• A nice design
Nice to have
• need it to look professional with a starting page that will work as a navigation. I need like logo and phone number and such up top, a picture under it with one sentence as a slogan and under it 6 boxes to click to come to our different pages. Under it I want news etc.
• today www.kolrev.se
• want more like www.tralvik.se or www.bersona.se
Should not have
• To many different colours and a messy design.

```html
<!DOCTYPE html>
<html lang="sv">
<head>
<meta charset="utf-8">
<title>Kolrev – Cms Page</title>
<link href="https://fonts.googleapis.com/css2?family=Didact+Gothic&family=Montserrat:ital,wght@0,600;0,700;0,800;1,800&display=swap" rel="stylesheet">
<style>
:root{
  --green:#abd037;
  --green-dark:#8fb52a;
  --blue:#3176b5;
  --blue-dark:#2b5f96;
  --grey:#9d9d9d;
  --grey-light:#aaaaaa;
  --line:#e3e3e3;
  --text:#4a4a4a;
  --head:#2c2c2c;
  --red:#f04a50;
}
*{margin:0;padding:0;box-sizing:border-box}
html,body{width:1200px;height:3905px;overflow:hidden;background:#fff}
body{position:relative;font-family:"Didact Gothic",sans-serif;color:var(--text);font-size:13px;line-height:1.55}
.abs{position:absolute}
h2,h3,h4{font-family:"Montserrat",sans-serif;color:var(--head)}
p{text-align:justify}

/* header */
.site-header{left:0;top:0;width:1200px;height:100px;background:#fff}
.brand{left:143px;top:14px;display:flex;align-items:center;gap:10px}
.brand-dot{width:46px;height:46px;border-radius:50%;background:var(--green)}
.brand-name{font-family:"Montserrat",sans-serif;font-weight:800;font-size:32px;color:var(--blue-dark);letter-spacing:1px}
.topbar{left:510px;top:0;width:690px;height:30px;background:var(--blue-dark);display:flex;align-items:center;padding-left:40px;gap:26px;color:#fff;font-size:12px}
.topbar .social{display:flex;gap:10px;margin-right:18px}
.topbar .social span{width:9px;height:9px;border-radius:50%;background:#fff}
.contact-row{left:490px;top:50px;display:flex;align-items:center;gap:40px;font-size:15px;color:#333}
.contact-row .item{display:flex;align-items:center;gap:8px}
.contact-row svg{width:18px;height:18px}
.menu-btn{left:1024px;top:50px;width:32px;height:32px;border-radius:50%;background:var(--green);display:flex;flex-direction:column;justify-content:center;align-items:center;gap:3px}
.menu-btn i{display:block;width:14px;height:2px;background:#fff}

/* hero */
.hero{left:0;top:100px;width:1200px;height:316px;background:linear-gradient(120deg,#5a5d4c 0%,#8a7a64 45%,#a7896d 60%,#4d5248 100%)}
.hero-slogan{left:143px;top:190px;font-family:"Montserrat",sans-serif;font-weight:800;font-style:italic;font-size:33px;line-height:1.2;color:#fff}
.hero-slogan .accent{color:var(--green)}
.hero-rule{left:305px;top:208px;width:250px;height:2px;background:#fff}
.hero-dots{left:584px;top:386px;display:flex;gap:6px}
.hero-dots span{width:8px;height:8px;border-radius:50%;background:#fff;opacity:.6}
.hero-dots span.on{background:var(--green);opacity:1}

.breadcrumb{left:0;top:416px;width:1200px;height:32px;background:#f2f2f2;padding-left:143px;display:flex;align-items:center;gap:8px;font-size:12px;color:#555}

/* page title */
.title-mark{left:586px;top:528px;width:30px;height:30px;border-radius:50%;background:var(--green)}
.page-title{left:0;top:580px;width:1200px;text-align:center;font-size:26px;font-weight:700;color:#555}

.media{background:#ccc}
.rule{left:143px;width:914px;height:1px;background:var(--line)}
.lead{font-size:17px;font-weight:700;line-height:1.4}
.sub{font-size:15px;font-weight:600}

.checklist{display:grid;grid-template-columns:repeat(5,1fr);row-gap:4px;font-size:12px}
.checklist li{list-style:none;display:flex;align-items:center;gap:6px}
.checklist li::before{content:"";width:6px;height:6px;border-right:2px solid var(--green);border-top:2px solid var(--green);transform:rotate(45deg)}

/* footer */
.site-footer{left:0;top:3600px;width:1200px;height:271px;background:var(--green)}
.foot-col{color:#fff;font-size:12px}
.foot-col h4{color:#fff;font-size:15px;font-weight:700;margin-bottom:18px}
.foot-col li{list-style:none;margin-bottom:10px;display:flex;align-items:center;gap:8px}
.foot-col li::before{content:"";width:5px;height:5px;border-radius:50%;background:#fff}
.foot-contact .row{display:flex;gap:10px;margin-bottom:14px;align-items:flex-start}
.foot-contact svg{width:15px;height:15px;flex:none}
.map{left:656px;top:3696px;width:182px;height:116px;background:linear-gradient(135deg,#eceae4,#d9dcd2)}
.map-pin{left:738px;top:3730px}
.foot-brand{left:920px;top:3660px;font-family:"Montserrat",sans-serif;font-weight:800;font-size:30px;color:#fff;opacity:.85}
.foot-social{left:960px;top:3712px;display:flex;gap:10px}
.foot-social span{width:10px;height:10px;border-radius:50%;background:#fff}
.bottom-bar{left:0;top:3871px;width:1200px;height:34px;background:var(--blue);color:#fff;font-size:12px;display:flex;align-items:center;justify-content:space-between;padding:0 143px}
</style>
</head>
<body>

<header class="abs site-header">
  <div class="abs brand"><span class="brand-dot"></span><span class="brand-name">Kolrev</span></div>
  <nav class="abs topbar">
    <div class="social"><span></span><span></span><span></span></div>
    <span>Kolrev Öppenvård</span><span>Stödboende</span><span>Vårdbehandling</span><span>Om Oss</span><span>Sök placering</span>
  </nav>
  <div class="abs contact-row">
    <div class="item"><svg viewBox="0 0 24 24"><path d="M6 3l4 1 1 5-2 2a12 12 0 005 5l2-2 5 1 1 4-3 2C10 21 3 14 3 6z" fill="#777"/></svg>010-4417260</div>
    <div class="item"><svg viewBox="0 0 24 24"><rect x="3" y="6" width="18" height="12" fill="none" stroke="#777" stroke-width="2"/><path d="M3 6l9 7 9-7" fill="none" stroke="#777" stroke-width="2"/></svg>info@kolrev.se</div>
    <div class="item"><svg viewBox="0 0 24 24"><circle cx="12" cy="12" r="9" fill="none" stroke="#777" stroke-width="2"/><path d="M12 7v5l3 3" stroke="#777" stroke-width="2" fill="none"/></svg>Måndag - Fredag 08:00 - 20:00</div>
  </div>
  <div class="abs menu-btn"><i></i><i></i><i></i></div>
</header>

<section class="abs hero" role="img" aria-label="Händer som håller en kruka med jord och en ung planta"></section>
<div class="abs hero-rule"></div>
<h1 class="abs hero-slogan">“ Vi Skapar<br><span class="accent">Hållbara Vägar Till<br>En Bättre Framtid.”</span></h1>
<div class="abs hero-dots"><span></span><span class="on"></span><span></span></div>

<div class="abs breadcrumb">Hem <span>›</span> Cms Page</div>

<span class="abs title-mark"></span>
<h2 class="abs page-title">CMS PAGE</h2>

<!-- block 1 -->
<div class="abs media" style="left:143px;top:656px;width:435px;height:268px;background:linear-gradient(135deg,#8b6e4e,#c9a57a 50%,#6d5a46)" role="img" aria-label="Videospelare med en hammare och spik på trägolv">
  <svg class="abs" style="left:194px;top:113px" width="46" height="32" viewBox="0 0 46 32"><rect width="46" height="32" rx="8" fill="var(--red)"/><path d="M18 9l12 7-12 7z" fill="#fff"/></svg>
  <div class="abs" style="left:0;bottom:0;width:435px;height:22px;background:rgba(0,0,0,.75)"></div>
</div>
<div class="abs" style="left:622px;top:652px;width:435px">
  <h3 class="lead">It is a long established fact that a reader will be distracted by the readable content.</h3>
  <p style="margin-top:10px">Lorem Ipsum is simply dummy text of the printing and typesetting industry. Lorem Ipsum has been the industry's standard dummy text ever since the 1500s, when an unknown printer took a galley of type and scrambled it to make a type specimen book. It has survived not only five centuries, but also the leap into electronic typesetting, remaining essentially unchanged. It was popularised in the 1960s with the release of Letraset sheets containing Lorem Ipsum passages, and more recently with desktop publishing software like Aldus PageMaker including versions of Lorem Ipsum.It is a long established fact that a reader will be distracted by the readable content of a page when looking at its layout.</p>
</div>
<div class="abs rule" style="top:968px"></div>

<!-- block 2 -->
<div class="abs" style="left:143px;top:1020px;width:435px">
  <h3 class="lead">It is a long established fact that a reader will be distracted by the readable content.</h3>
  <p style="margin-top:10px">Lorem Ipsum is simply dummy text of the printing and typesetting industry. Lorem Ipsum has been the industry's standard dummy text ever since the 1500s, when an unknown printer took a galley of type and scrambled it to make a type specimen book. It has survived not only five centuries, but also the leap into electronic typesetting, remaining essentially unchanged. It was popularised in the 1960s with the release of Letraset sheets containing Lorem Ipsum passages, and more recently with desktop publishing software like Aldus PageMaker including versions of Lorem Ipsum.It is a long established fact that a reader will be distracted by the readable content of a page when looking at its layout.</p>
</div>
<div class="abs media" style="left:622px;top:1020px;width:435px;height:274px;background:linear-gradient(135deg,#e8e4dc,#b9ab98 55%,#6b5d50)" role="img" aria-label="Ljust vardagsrum med soffa, tv och fönster"></div>
<div class="abs rule" style="top:1348px"></div>

<!-- block 3 -->
<div class="abs" style="left:143px;top:1394px;width:914px">
  <h3 class="sub">All the Lorem Ipsum generators on the Internet tend to repeat predefined chunks as necessary</h3>
  <p style="margin-top:10px">There are many variations of passages of Lorem Ipsum available, but the majority have suffered alteration in some form, by injected humour, or randomised words which don't look even slightly believable. If you are going to use a passage of Lorem Ipsum, you need to be sure there isn't anything embarrassing hidden in the middle of text. All the Lorem Ipsum generators on the Internet tend to repeat predefined chunks as necessary, making this the first true generator on the Internet.</p>
</div>
<div class="abs rule" style="top:1557px"></div>

<!-- block 4 -->
<h3 class="abs sub" style="left:143px;top:1598px;width:914px">All the Lorem Ipsum generators on the Internet tend to repeat predefined chunks as necessary.</h3>
<div class="abs media" style="left:143px;top:1640px;width:914px;height:273px;background:linear-gradient(120deg,#2e2620,#5b4636 45%,#3a2f27)" role="img" aria-label="Hand som planterar små gröna plantor i svarta krukor"></div>
<div class="abs" style="left:143px;top:1930px;width:914px">
  <p>There are many variations of passages of Lorem Ipsum available, but the majority have suffered alteration in some form, by injected humour, or randomised words which don't look even slightly believable. If you are going to use a passage of Lorem Ipsum, you need to be sure there isn't anything embarrassing hidden in the middle of text. All the Lorem Ipsum generators on the Internet tend to repeat predefined chunks as necessary, making this the first true generator on the Internet.</p>
  <p style="margin-top:16px">There are many variations of passages of Lorem Ipsum available, but the majority have suffered alteration in some form, by injected humour, or randomised words which don't look even slightly believable. If you are going to use a passage of Lorem Ipsum, you need to be sure there isn't anything embarrassing hidden in the middle of text. All the Lorem Ipsum generators on the Internet tend to repeat predefined chunks as necessary, making this the first true generator on the Internet. It uses a dictionary of over 200 Latin words, combined with a handful of model sentence structures, to generate Lorem Ipsum which looks reasonable. The generated Lorem Ipsum is therefore always free from repetition, injected humour, or non-characteristic words etc.</p>
</div>
<div class="abs rule" style="top:2200px"></div>

<!-- block 5 -->
<div class="abs media" style="left:143px;top:2330px;width:435px;height:208px;background:linear-gradient(180deg,#c9d3d9 0%,#c9d3d9 35%,#8c4a3a 36%,#7a4134 70%,#6e8a4a 72%)" role="img" aria-label="Rött tegelhus med gräsmatta"></div>
<div class="abs media" style="left:622px;top:2330px;width:435px;height:208px;background:linear-gradient(180deg,#d8dfe4 0%,#d8dfe4 38%,#8e3b33 40%,#7d352e 68%,#7f9a52 70%)" role="img" aria-label="Rött trähus med vita knutar på gräsplan"></div>
<div class="abs" style="left:143px;top:2560px;width:435px">
  <h3 class="lead">Lorem Ipsum is simply dummy text of the printing and typesetting industry.</h3>
  <p style="margin-top:12px">There are many variations of passages of Lorem Ipsum available, but the majority have suffered alteration in some form, by injected humour, or randomised words which don't look even slightly believable. If you are going to use a passage of Lorem Ipsum, you need to be sure there isn't anything embarrassing hidden in the middle of text. All the Lorem Ipsum generators on the Internet tend to repeat predefined chunks as necessary, making this the first true generator on the Internet.</p>
</div>
<div class="abs" style="left:622px;top:2560px;width:435px">
  <h3 class="lead">Lorem Ipsum is simply dummy text of the printing and typesetting industry.</h3>
  <p style="margin-top:12px">There are many variations of passages of Lorem Ipsum available, but the majority have suffered alteration in some form, by injected humour, or randomised words which don't look even slightly believable. If you are going to use a passage of Lorem Ipsum, you need to be sure there isn't anything embarrassing hidden in the middle of text. All the Lorem Ipsum generators on the Internet tend to repeat predefined chunks as necessary, making this the first true generator on the Internet.</p>
</div>
<div class="abs rule" style="top:2811px"></div>

<!-- block 6 -->
<div class="abs" style="left:143px;top:2846px;width:914px">
  <h3 class="sub">All the Lorem Ipsum generators on the Internet tend to repeat predefined chunks as necessary.</h3>
  <p style="margin-top:8px">Lorem Ipsum has been the industry's standard dummy text ever since the 1500s, when an unknown printer took a galley of type and scrambled it to make a type specimen book. It has survived not only five centuries, but also the leap into electronic typesetting.</p>
  <ul class="checklist" style="margin-top:16px">
    <li>At Vero Eos Et Accusamus</li><li>At Vero Eos Et Accusamus</li><li>At Vero Eos Et Accusamus</li><li>At Vero Eos Et Accusamus</li><li>At Vero Eos Et Accusamus</li>
    <li>Iusto Odio Dignissimos</li><li>Iusto Odio Dignissimos</li><li>Iusto Odio Dignissimos</li><li>Iusto Odio Dignissimos</li><li>Iusto Odio Dignissimos</li>
    <li>Nam Libero Tempore</li><li>Nam Libero Tempore</li><li>Nam Libero Tempore</li><li>Nam Libero Tempore</li><li>Nam Libero Tempore</li>
    <li>Voluptatibus Maiores Alias</li><li>Voluptatibus Maiores Alias</li><li>Voluptatibus Maiores Alias</li><li>Voluptatibus Maiores Alias</li><li>Voluptatibus Maiores Alias</li>
  </ul>
</div>
<div class="abs rule" style="top:3072px"></div>

<!-- block 7 -->
<div class="abs media" style="left:143px;top:3131px;width:279px;height:209px;background:linear-gradient(180deg,#a9c8e6 0%,#a9c8e6 35%,#e9e6e0 36%,#cfc8bd 65%,#5e9a3a 67%)" role="img" aria-label="Vitt villahus med grön gräsmatta"></div>
<div class="abs media" style="left:456px;top:3131px;width:281px;height:209px;background:linear-gradient(180deg,#9ec0e0 0%,#9ec0e0 35%,#a27a5c 36%,#8a6650 65%,#6b9a44 67%)" role="img" aria-label="Stort bostadshus i sten och trä"></div>
<div class="abs media" style="left:773px;top:3131px;width:284px;height:209px;background:linear-gradient(180deg,#c8d6e2 0%,#c8d6e2 38%,#9a5a48 40%,#86503f 66%,#9aa66a 68%)" role="img" aria-label="Tegelbyggnad med gårdsplan"></div>
<div class="abs" style="left:143px;top:3362px;width:279px">
  <h3 class="lead" style="font-size:16px">It is a long established facts reader of lorem ipsum dolor amet.</h3>
  <p style="margin-top:12px">There are many variations of passages of Lorem Ipsum available, but the majority have suffered alteration in some form, by injected humour, or randomised words which don't look even slightly believable.</p>
</div>
<div class="abs" style="left:456px;top:3362px;width:281px">
  <h3 class="lead" style="font-size:16px">It is a long established facts reader of lorem ipsum dolor amet.</h3>
  <p style="margin-top:12px">If you are going to use a passage of Lorem Ipsum, you need to be sure there isn't anything embarrassing hidden in the middle of text. All the Lorem Ipsum generators on the Internet tend to repeat predefined chunks as necessary.</p>
</div>
<div class="abs" style="left:773px;top:3362px;width:284px">
  <h3 class="lead" style="font-size:16px">It is a long established facts reader of lorem ipsum dolor amet.</h3>
  <p style="margin-top:12px">If you are going to use a passage of Lorem Ipsum, you need to be sure there isn't anything embarrassing hidden in the middle of text. All the Lorem Ipsum generators on the Internet tend to repeat predefined chunks as necessary.</p>
</div>

<!-- footer -->
<footer class="abs site-footer"></footer>
<div class="abs foot-col" style="left:143px;top:3650px">
  <h4>Snabblänkar</h4>
  <ul><li>Kolrev Öppenvård</li><li>Stödboende</li><li>Vård Adressat</li><li>Om Oss</li><li>Placeringsförfrågan</li></ul>
</div>
<div class="abs foot-col foot-contact" style="left:360px;top:3650px">
  <h4>Kontaktuppgifter</h4>
  <div class="row"><svg viewBox="0 0 24 24"><path d="M12 2a7 7 0 017 7c0 5-7 13-7 13S5 14 5 9a7 7 0 017-7z" fill="#fff"/></svg><div><b>Kolrev Sverige AB</b><br>Lindgatan 12, 262 91 Åsby</div></div>
  <div class="row"><svg viewBox="0 0 24 24"><path d="M6 3l4 1 1 5-2 2a12 12 0 005 5l2-2 5 1 1 4-3 2C10 21 3 14 3 6z" fill="#fff"/></svg>010-4417260</div>
  <div class="row"><svg viewBox="0 0 24 24"><rect x="3" y="6" width="18" height="12" fill="none" stroke="#fff" stroke-width="2"/><path d="M3 6l9 7 9-7" fill="none" stroke="#fff" stroke-width="2"/></svg>info@kolrev.se</div>
</div>
<div class="abs foot-col" style="left:656px;top:3650px"><h4>Plats Karta</h4></div>
<div class="abs map" role="img" aria-label="Karta som visar kontorets läge"></div>
<svg class="abs map-pin" width="16" height="22" viewBox="0 0 24 32"><path d="M12 0a12 12 0 0112 12c0 9-12 20-12 20S0 21 0 12A12 12 0 0112 0z" fill="var(--red)"/><circle cx="12" cy="12" r="4" fill="#fff"/></svg>
<div class="abs foot-brand">Kolrev</div>
<div class="abs foot-social"><span></span><span></span><span></span></div>
<div class="abs bottom-bar"><span>Upphovsrätt 2018 Kolrev Sverige AB. Alla rättigheter förbehållna.</span><span>Användarvillkor | Integritetspolicy</span></div>

</body>
</html>
```